Custom Apparel Decorating Company needs a Website Home Page Banner Design

We are in need of a website Home page banner design for a small company based in Canada called Quelvana. We are a custom apparel company that offers custom apparel (t-shirts, hoodies, hats etc) to Companies, Organizations/groups, bands, Spirit wear and individuals. We would like the design to match with the logo files we have attached to the campaign. The Website has not been created yet planning to tie the website into the home page banner for flow. Thinking of using Duda or Shopify for the website if that helps! We are really looking forward to seeing the designs.

Target Market(s)

Companies, Organizations/Groups, Bands, Spirit wear and Individuals. Anyone that is looking to have there company or own logo/Design put on a piece of clothing.

Requirements
Must have
• -Colours in the logo files.
• -FUN creating the Home Page Banner!!! :)
Nice to have
• -Up Beat feel to it (it's the first image you will see when you go to the website, it's the store front so we want to grab the attention of the potential customers)

```html
<!DOCTYPE html>
<html lang="en">
<head>
<meta charset="UTF-8">
<title>Quelvana – Home Banner</title>
<link href="https://fonts.googleapis.com/css2?family=Poppins:wght@200;300;700;800&display=swap" rel="stylesheet">
<style>
  :root {
    --sky: #12a6fb;
    --coral: #e8393b;
    --white: #ffffff;
    --ghost: rgba(255, 255, 255, 0.12);
    --jacket-navy: #1d3f9c;
    --jacket-blue: #2147b4;
    --hair-blond: #e6cfa4;
    --denim: #5a8cc4;
  }
  * { margin: 0; padding: 0; box-sizing: border-box; }
  html, body { width: 1200px; height: 450px; overflow: hidden; }
  body { font-family: "Poppins", sans-serif; color: var(--white); }

  .banner { position: relative; width: 1200px; height: 450px; overflow: hidden; }

  .panel { position: absolute; top: 0; width: 600px; height: 450px; overflow: hidden; }
  .panel--men { left: 0; background: var(--sky); }
  .panel--women { left: 600px; background: var(--coral); }

  .ghost-word {
    position: absolute;
    font-weight: 700;
    font-size: 100px;
    line-height: 1;
    white-space: nowrap;
    letter-spacing: -1px;
    color: var(--ghost);
  }
  .panel--men .ghost-word { right: 38px; top: 340px; }
  .panel--women .ghost-word { left: 38px; top: 8px; }

  .photo {
    position: absolute;
    -webkit-mask-image: radial-gradient(ellipse 60% 75% at 50% 60%, #000 55%, transparent 100%);
            mask-image: radial-gradient(ellipse 60% 75% at 50% 60%, #000 55%, transparent 100%);
  }
  .photo--man {
    left: 20px; top: 0; width: 370px; height: 450px;
    background: linear-gradient(180deg, var(--jacket-navy) 0%, var(--jacket-blue) 60%, var(--jacket-navy) 100%);
    opacity: 0.75;
  }
  .photo--woman {
    left: 250px; top: 0; width: 270px; height: 450px;
    background: linear-gradient(180deg, var(--hair-blond) 0%, var(--denim) 45%, var(--denim) 100%);
    opacity: 0.8;
  }

  .copy { position: absolute; }
  .copy--men { left: 396px; top: 110px; width: 204px; }
  .copy--women { left: 600px; top: 191px; width: 204px; text-align: right; }

  .headline {
    font-weight: 800;
    font-size: 40px;
    line-height: 1;
  }
  .rule { height: 3px; width: 204px; background: var(--white); margin: 12px 0 9px; }

  .subline {
    font-weight: 200;
    font-size: 24px;
    line-height: 27px;
    letter-spacing: 0.3px;
    white-space: nowrap;
  }

  .cta {
    display: inline-block;
    margin-top: 11px;
    height: 27px;
    padding: 0 17px;
    border-radius: 14px;
    font-weight: 700;
    font-size: 10.5px;
    line-height: 27px;
    color: var(--white);
    text-decoration: none;
  }
  .cta--coral { background: var(--coral); }
  .cta--sky { background: var(--sky); padding: 0 16px; }
</style>
</head>
<body>
  <main class="banner">
    <section class="panel panel--men">
      <span class="ghost-word" aria-hidden="true">Quelvana</span>
      <div class="photo photo--man" role="img" aria-label="Photo of a man in a backwards cap, blue zip jacket and white printed t-shirt"></div>
    </section>

    <section class="panel panel--women">
      <span class="ghost-word" aria-hidden="true">Quelvana</span>
      <div class="photo photo--woman" role="img" aria-label="Photo of a smiling blonde woman in a blue denim jacket"></div>
    </section>

    <div class="copy copy--men">
      <h2 class="headline">Summer</h2>
      <div class="rule"></div>
      <p class="subline">Custom apparel<br>for men's</p>
      <a class="cta cta--coral" href="#">View Collection</a>
    </div>

    <div class="copy copy--women">
      <h2 class="headline">Inspired</h2>
      <div class="rule"></div>
      <p class="subline">Custom Denim<br>for women</p>
      <a class="cta cta--sky" href="#">View Collection</a>
    </div>
  </main>
</body>
</html>
```